Harmonia Women's Clinic - patient info e-book

We require an easy-edit template for a patient e-book that can easily be converted into a pdf for distribution through our website.
**We will be using Adobe InDesign, so compatible designs ONLY will be considered**
Target Market(s)
Women aged 28-55
Industry/Entity Type
Health
Font styles to use
Sans Serif
Colors
886aae
b8a6cd
d3a5cc
b768aa
ffffff
ecdaeb
b868aa
fbd4d5
f59296
Requirements
Must have
- Editable fields for text
- Easy to convert to PDF
- Easy to insert/change stock photos
- Should incorporate the attached logo

```html
<!DOCTYPE html>
<html lang="en">
<head>
<meta charset="utf-8">
<title>Closing Thoughts – Harmonia Women's Clinic News</title>
<link rel="stylesheet" href="https://fonts.googleapis.com/css2?family=Open+Sans:wght@600;700&family=Tinos:ital,wght@0,400;1,400&display=swap">
<style>
  :root {
    --purple: #886aae;
    --purple-light: #b8a6cd;
    --salmon: #f59296;
    --ink: #1c1c1c;
    --shadow: #4a4a4a;
    --paper: #ffffff;
    --photo-top: #d8d2cc;
    --photo-bottom: #6f7f8a;
  }
  * { box-sizing: border-box; margin: 0; padding: 0; }
  html, body { width: 927px; height: 1200px; overflow: hidden; background: var(--paper); }
  .page { position: relative; width: 927px; height: 1200px; overflow: hidden; background: var(--paper); color: var(--ink); font-family: "Tinos", "Times New Roman", serif; }

  .section-band { position: absolute; left: 0; top: 0; width: 927px; height: 94px; background: var(--purple); border-bottom: 5px solid var(--shadow); }
  .section-band__label { position: absolute; left: 57px; top: 54px; font-family: "Open Sans", Arial, sans-serif; font-weight: 700; font-size: 23px; color: var(--paper); line-height: 1; }

  .headline { position: absolute; left: 57px; top: 118px; font-family: "Open Sans", Arial, sans-serif; font-weight: 700; font-size: 50px; color: var(--salmon); line-height: 1; letter-spacing: -0.3px; }

  .column { position: absolute; font-size: 15.4px; line-height: 20.3px; letter-spacing: -0.1px; text-align: justify; hyphens: manual; }
  .column p { text-indent: 30px; margin-bottom: 10px; }
  .column p:last-child { margin-bottom: 0; }
  .column--one { left: 58px; top: 230px; width: 245px; }
  .column--two { left: 336px; top: 230px; width: 244px; }
  .column--two p { text-indent: 0; }
  .column--three { left: 618px; top: 620px; width: 255px; }
  .column--three p.lead { text-indent: 0; }

  .portrait { position: absolute; left: 618px; top: 142px; width: 255px; height: 297px; border: 2px solid var(--ink); background: linear-gradient(180deg, var(--photo-top) 0%, var(--photo-bottom) 100%); }
  .portrait__caption { position: absolute; left: 618px; top: 455px; width: 255px; text-align: center; font-style: italic; font-size: 15.4px; }

  .divider { position: absolute; left: 618px; top: 501px; width: 255px; height: 5px; background: var(--purple); }

  .sidebar-heading { position: absolute; left: 618px; top: 522px; width: 255px; font-family: "Open Sans", Arial, sans-serif; font-weight: 600; font-size: 24.5px; line-height: 32px; }
  .sidebar-note { position: absolute; left: 618px; top: 588px; font-style: italic; font-size: 15.4px; }

  .folio { position: absolute; top: 1143px; font-family: "Open Sans", Arial, sans-serif; font-weight: 700; font-size: 15.5px; line-height: 1; }
  .folio--left { left: 28px; }
  .folio--right { right: 57px; }
</style>
</head>
<body>
<main class="page">
  <header class="section-band">
    <span class="section-band__label">Closing Thoughts...</span>
  </header>

  <h1 class="headline">Evel magnis et</h1>

  <section class="column column--one">
    <p>Dia ilitem verem et mos num, aut eata quid eatio. Fici omnimaio. Den&shy;digent quatemp erspere mporrum in&shy;tur? Quia sitium fugitio. Ehende min core quis eum earchil idellamus repero maio eos ant.</p>
    <p>Henimaion core parum inus, ul&shy;lates ciumqui blabo. Agnis mil ius aut eatem aut ma quiam, consecae. Ulpa adia voluptis aute venimus nulluptas quate nonem apist haribeatur? Quisi&shy;ma si dolorit, ut audis dolore quodi to con earum laborep elesequae nest qui con peri as as es ates eaqui debit mo&shy;luptis voluptat adiamusdae. Obitempor sin poribus repeles aut ad ut dolendis arum quae officat mint.</p>
    <p>Ullaboraest, consequi num ute nonse dolest rem fugitat ibeaquae ni alibus, con estem sersper natio. Ut repere poriore vendignis es eicium aligend aectur? Musa vel essum hic&shy;itemquia corrum doluptatur a a derio. Ur, odi cum aspernam hit omnimet quidebit et estemquiae. Il isti iditinus, optatest quam rectiis ex et ipit labor&shy;rum eum del mosapel lectatibus acien&shy;tur asitiatin nest, verferuptur maxim eum rem enes ut atecume velest officia quatur alitiam a velit ipsande necti&shy;atus volo des nus rem re non ped ex et eictibea dolut lant dunt accus modicia sinimentio. Et labo. Nihictiaeped que none re inullorupta net magnia none et lit qui offictu sandeles aspitius quosse&shy;que numqui sim aut ex earum dolum faccus.</p>
    <p>On remqui sere nim illabor epu&shy;daest aut rehent et aliqui iustist, solup&shy;tas cusam, sum inciment Ehende sitia&shy;tur alic tendes dolupid molor ant.</p>
    <p>Niatur sima veruptia quid ullia saped quam eum et dipitenderes di</p>
  </section>

  <section class="column column--two">
    <p>sandita ectiam, qui vitiusdae volup&shy;ta apelestium eat omni dolorro vitaes arcitio. Occus, temqui di nimus dollor alique nienimp oremporepuda vende nes conseque commod que vel im di demporit labore, ut voluptatur apidRo tem faciani mintibus aut faceaqui quidist, nobitem volum fugit utem re doluptist res magnis volorehentem hil&shy;litatem ipsumqu isitias aut re elenda&shy;mus aut volentem quias ut eos dolupta&shy;tium quidisto velecum repudam que explabo. Nulpa viditam, volendandem. Odion nihillab im que essimil eatum ipiendae. Nem fugit enia quatqua ep&shy;tur? Haruptati beruntet velitio nsedion perem quatem. Te landucimus consed et fuga. Ut quos dit odit aut molessi ni&shy;hilibeatur a explis rernatis volupta am quo ium ipsum ventempos excerioria volorensis sequia senis eossequas ut et, ut quisit apel evendam quias et, que nulpa dunt laborro in rerem erio ver&shy;rorrum dera nonem reptat faces ace&shy;rioribus es magnihilia sapeles cillend eliquid quis eturecti cus sit ese alibus eserum il idipsum volute volorpor ali&shy;quam haritiati conseque volest eri re&shy;peligendi volupiet inventenis et vellitet fugia iur? Ro blacipid quidelit reicid modi in consect invelia dolora sitiume sequundio et que in cum que vel ea voluptatio. Nam untur, es et eiciustiur sanda eum rerios alia verferchit ullaut plaborum ratecep udipis ex et quis ius eatur reprem enditatiusda perfero odi&shy;onem audit, con parum quisqui quat dipis cusa esto expe con cum rae vol&shy;orrovid ut explaborro tem acepratiorro blab ipsament in nihil iunt ipsam et, soluptatem. Dolo qui con evelluptatur si aut eaquiatis rendund ipsandi offi&shy;ciuscius ut omni aut milit mosant aut</p>
  </section>

  <figure>
    <div class="portrait" role="img" aria-label="Portrait photograph of a smiling woman with curly hair and glasses"></div>
    <figcaption class="portrait__caption">Nam que pla simille catibus, siminis</figcaption>
  </figure>

  <div class="divider"></div>

  <h2 class="sidebar-heading">Mi, et que ped que volorei ustrumquo</h2>
  <p class="sidebar-note">continuted from page one</p>

  <section class="column column--three">
    <p class="lead">que lam as earunt.</p>
    <p>Puda pa voluptaquae. Nam fugit maionsent quam rendiostrum ideb&shy;it evelitatiis accuptaqui arum sequos everi coreped ut quossime dolorio vel ius, que endam expe sintoribus pratur&shy;is coreicabore eatusda voloriat.</p>
    <p>Sunto dist aut faces maionse&shy;qui tesseca borempores doluptatem harchil eossimin es atquuntis ma pel molo min eos magnihil ilibeaque ever&shy;fere nectota sus que sintius, tet hil es&shy;sed earupta ius re dolupiet ut duciend&shy;unt ea suntum conetur aut qui aut qui dTem fugitium nonsecus sunt, natur autemos velent quoditibusam sit dolu&shy;pieniet auda volupiciam vero dolorem&shy;porem aliquat usapis essum aut quisci dolorem que volum nullibe atectem. Ximendis voluptat et parum et erist di doloris et eost laborum essumque per&shy;ore omnis sin exeribusti idebis eum ut alita sit auta consequi dolest, vollabo&shy;rum dioribernam conse</p>
  </section>

  <footer>
    <span class="folio folio--left">4 &nbsp;Harmonia Women's Clinic News</span>
    <span class="folio folio--right">May 2015</span>
  </footer>
</main>
</body>
</html>
```